Colorful Dog Trainer Business cards

I need a logo that's an illustration of my dog's head - ideally just line work. It will also include my business name (MARLO BRISK CO), Positive Reinforcement Training, my name, my certifications, phone, email, and instagram. Creative card shapes are welcome! I want it to be colorful and eye catching.
Target Market(s)
dog owners in Manhattan and Jersey City
Industry/Entity Type
dog training
Contact Information for Business Card
my business name (MARLO BRISK CO), Positive Reinforcement Training, my name, my certifications, phone, email, and instagram
Look and feel

```html
<!DOCTYPE html>
<html lang="en">
<head>
<meta charset="utf-8">
<title>Marlo Brisk Co — Business Cards</title>
<link rel="stylesheet" href="https://fonts.googleapis.com/css2?family=Montserrat:wght@500;600;700&family=Poppins:wght@400;500;600;700&display=swap">
<style>
  :root {
    --brown: #8b5a3f;
    --brown-deep: #6e4430;
    --ink: #1d1916;
    --grey: #686868;
    --grey-light: #a9a9a9;
    --white: #ffffff;
    --page: #f4f2f0;
  }
  * { box-sizing: border-box; margin: 0; padding: 0; }
  html, body { width: 1200px; height: 2259px; overflow: hidden; background: var(--page); }
  body { position: relative; font-family: "Poppins", sans-serif; }

  .card {
    position: absolute; left: 90px; width: 1020px; height: 582px;
    background: var(--brown); overflow: hidden;
    box-shadow: 0 8px 24px rgba(0,0,0,.28);
  }
  .card--front { top: 498px; }
  .card--back { top: 1180px; }

  .card__shapes { position: absolute; inset: 0; }

  .mark-art {
    position: absolute; border-radius: 50%;
    border: 4px solid var(--ink);
    background: radial-gradient(circle at 50% 45%, #4a4340 0%, #2e2a28 55%, #7a4f38 100%);
  }
  .brand {
    position: absolute; text-align: center;
    font-family: "Poppins", sans-serif; font-weight: 600; color: var(--ink);
    letter-spacing: -1px; white-space: nowrap; line-height: 1;
  }
  .tagline {
    position: absolute; text-align: center; white-space: nowrap;
    font-family: "Poppins", sans-serif; font-weight: 500; color: var(--ink);
    letter-spacing: 3.4px; line-height: 1;
  }

  /* front */
  .card--front .mark-art { left: 141px; top: 88px; width: 236px; height: 236px; }
  .card--front .brand { left: 0; width: 518px; top: 344px; font-size: 38px; }
  .card--front .tagline { left: 0; width: 518px; top: 399px; font-size: 13px; }

  .cert-list { position: absolute; left: 61px; top: 453px; width: 404px; list-style: none; }
  .cert {
    height: 27px; margin-bottom: 16px; border-radius: 7px; background: var(--white);
    color: var(--brown); font-weight: 600; font-size: 20px; line-height: 27px;
    text-align: center; letter-spacing: .3px;
  }

  .contact-block { position: absolute; left: 586px; top: 128px; right: 0; }
  .person__name {
    font-family: "Montserrat", sans-serif; font-weight: 600; font-size: 49px;
    color: var(--brown); line-height: 1; letter-spacing: .3px;
  }
  .person__role {
    display: flex; align-items: center; gap: 14px; margin-top: 6px;
    font-size: 25px; color: var(--ink); line-height: 1;
  }
  .person__role::after { content: ""; flex: 1; height: 2px; background: var(--brown); }

  .contact-list { list-style: none; margin-top: 40px; }
  .contact {
    display: flex; align-items: center; height: 48px;
    font-size: 25px; color: var(--ink);
  }
  .contact__icon { width: 28px; height: 28px; margin: 0 21px 0 10px; flex: none; }

  /* back */
  .card--back .mark-art { left: 375px; top: 57px; width: 272px; height: 272px; }
  .card--back .brand { left: 0; width: 1020px; top: 358px; font-size: 52px; }
  .card--back .tagline { left: 0; width: 1020px; top: 425px; font-size: 15px; }
  .band { position: absolute; left: 0; right: 0; top: 493px; bottom: 0; background: var(--grey); }
  .band::before { content: ""; position: absolute; left: 0; right: 0; top: -5px; height: 2px; background: var(--white); }
  .web-pill {
    position: absolute; left: 277px; top: 473px; width: 478px; height: 40px;
    border-radius: 10px; background: var(--white);
    color: var(--brown); font-weight: 600; font-size: 28px; line-height: 40px;
    text-align: center; letter-spacing: 3px;
  }
</style>
</head>
<body>

<section class="card card--front" aria-label="Business card front">
  <svg class="card__shapes" viewBox="0 0 1020 582" width="1020" height="582" aria-hidden="true">
    <circle cx="795" cy="246" r="362" fill="var(--grey)"/>
    <circle cx="818" cy="236" r="334" fill="var(--grey-light)"/>
    <circle cx="822" cy="232" r="328" fill="var(--white)"/>
  </svg>

  <div class="mark-art" role="img" aria-label="Illustrated dog head emblem"></div>
  <p class="brand">MARLO BRISK CO</p>
  <p class="tagline">POSITIVE REINFORCEMENT TRAINING</p>
  <ul class="cert-list">
    <li class="cert">PROFESSIONAL CERTIFICATION</li>
    <li class="cert">PRACTITIONER CERTIFICATION</li>
  </ul>

  <div class="contact-block">
    <h1 class="person__name">Dana Holt</h1>
    <p class="person__role">Dog Trainer</p>
    <ul class="contact-list">
      <li class="contact">
        <svg class="contact__icon" viewBox="0 0 28 28" aria-hidden="true">
          <circle cx="14" cy="14" r="13" fill="var(--brown)"/>
          <path d="M9 8c1-1 2-1 2.5 0l1.3 2.6c.3.6 0 1.2-.5 1.6l-.8.6c.8 1.8 2 3 3.8 3.8l.6-.8c.4-.5 1-.8 1.6-.5l2.6 1.3c1 .5 1 1.5 0 2.5-1.4 1.4-3.5 1.2-6-.4-2-1.3-3.3-2.6-4.6-4.6C8 11.5 7.7 9.4 9 8z" fill="var(--white)"/>
        </svg>011 555 010 42</li>
      <li class="contact">
        <svg class="contact__icon" viewBox="0 0 28 28" aria-hidden="true">
          <path d="M2 15 26 3 18 26 13 17z" fill="var(--brown)"/>
          <path d="M13 17 26 3" stroke="var(--white)" stroke-width="1.5"/>
        </svg>info@marlobrisk.com</li>
      <li class="contact">
        <svg class="contact__icon" viewBox="0 0 28 28" aria-hidden="true">
          <circle cx="14" cy="14" r="13" fill="var(--brown)"/>
          <rect x="8.5" y="8.5" width="11" height="11" rx="1.5" fill="none" stroke="var(--white)" stroke-width="1.6"/>
        </svg>@marlobriskco</li>
      <li class="contact">
        <svg class="contact__icon" viewBox="0 0 28 28" aria-hidden="true">
          <circle cx="14" cy="14" r="13" fill="var(--brown)"/>
          <g fill="none" stroke="var(--white)" stroke-width="1.4">
            <circle cx="14" cy="14" r="7.5"/>
            <ellipse cx="14" cy="14" rx="3.3" ry="7.5"/>
            <path d="M6.5 14h15M8 10h12M8 18h12"/>
          </g>
        </svg>www.marlobrisk.com</li>
    </ul>
  </div>
</section>

<section class="card card--back" aria-label="Business card back">
  <div class="mark-art" role="img" aria-label="Illustrated dog head emblem"></div>
  <p class="brand">MARLO BRISK CO</p>
  <p class="tagline">POSITIVE REINFORCEMENT TRAINING</p>
  <div class="band"></div>
  <p class="web-pill">www.marlobrisk.com</p>
</section>

</body>
</html>
```